依頼概要
■依頼の目的/概要
小学生バレーボールのスポーツ少年団でメンバーを募集するためのポスターの作成をお願いします。

■依頼詳細
ポスターは男子チーム、女子チーム兼用となります。主に教室での直接配布、校内の掲示板や近隣の施設(コンビニや公民館等)での掲示を目的としたものになります。

必要に応じて写真の背景等を加工いただいても構いません。

楽しそうなイメージだけでなく、スポーツに関心のある子どもたちがバレーボールを“かっこいい”と感じてくれるような躍動感の伝わるものを希望しています。

■重視する点
・明るくインパクトのあるデザイン
・できるだけ躍動感の伝わるもの
・読みやすい文字であること

■サイズ
A4サイズでお願いします。
メインはA4ですが、B4(A4の122%)にも対応する画素数でお願いいたします

■その他
・レイアウトイメージ、素材は添付ファイルにてご確認ください
・写真やイラストの素材は当方で用意していますが、用意したもの以外の素材を使っていただいても構いません。
・レイアウトのイメージやキャッチコピー、掲載する文言等は添付の「レイアウトイメージ.pdf」「レイアウト説明.txt」を参照ください。レイアウトは当方のイメージと異なるものになっても構いません。

何かご不明な点がございましたら、お気軽にご質問下さい。
どうぞよろしくお願いいたします。
納品いただくデータですが、納品後に当方で編集することがあるため、フォトショップまたはイラストレーターで編集できるかたちで納品いただけますと幸いです。よろしくお願いします。

```html
<!DOCTYPE html>
<html lang="ja">
<head>
<meta charset="utf-8">
<title>大空バレースポーツ少年団 メンバー募集</title>
<link href="https://fonts.googleapis.com/css2?family=M+PLUS+Rounded+1c:wght@500;700;800;900&display=swap" rel="stylesheet">
<style>
:root{
  --brown:#7a3f1c;
  --brown-dark:#5a2c12;
  --orange:#c9561c;
  --orange-light:#e07a2c;
  --cream:#fbf3e2;
  --red:#d42a24;
  --yellow:#ffe45c;
  --green:#3aa35a;
  --green-dark:#23803f;
  --white:#ffffff;
  --photo-a:#b89a7a;
  --photo-b:#8b6f57;
}
*{box-sizing:border-box;margin:0;padding:0}
html,body{width:867px;height:1200px;overflow:hidden;background:#fff}
body{font-family:"M PLUS Rounded 1c",sans-serif;color:var(--brown-dark)}
.poster{position:relative;width:867px;height:1200px;
  background:repeating-linear-gradient(90deg,var(--orange) 0 28px,var(--orange-light) 28px 56px);overflow:hidden}
.header{position:absolute;left:0;top:0;width:867px;height:292px;background:var(--cream);
  border-bottom-left-radius:50% 40px;border-bottom-right-radius:50% 40px}
.title{position:absolute;left:0;right:0;top:26px;text-align:center;font-weight:900;font-size:66px;line-height:1.12;color:var(--brown);letter-spacing:4px}
.title span{display:block}
.kid{position:absolute;border-radius:40px;background:linear-gradient(160deg,#f2c9a0,#d9462f)}
.kid.left{left:20px;top:18px;width:140px;height:150px}
.kid.right{right:20px;top:18px;width:140px;height:150px;background:linear-gradient(200deg,#f2c9a0,#d9462f)}
.bubble-top{position:absolute;top:190px;font-size:16px;font-weight:800;line-height:1.35;color:var(--red)}
.bubble-top.left{left:30px}
.bubble-top.right{right:30px;text-align:right}
.collage{position:absolute;left:40px;top:306px;width:787px;height:250px;display:grid;grid-template-columns:1fr 1fr 1fr;grid-template-rows:1fr 1fr;gap:8px;padding:8px;background:var(--white);transform:rotate(-1deg)}
.photo{background:linear-gradient(135deg,var(--photo-a),var(--photo-b));border-radius:4px}
.photo.tall{grid-row:span 2}
.club-name{position:absolute;left:0;right:0;top:566px;text-align:center;font-size:44px;line-height:56px;font-weight:900;color:var(--yellow)}
.recruit{position:absolute;left:150px;width:567px;top:624px;height:58px;background:var(--red);border-radius:10px;text-align:center;font-size:44px;line-height:58px;font-weight:900;color:var(--white)}
.schedule{position:absolute;left:100px;right:100px;top:690px;color:var(--white);font-weight:800}
.schedule h3{text-align:center;font-size:22px;line-height:30px;margin-bottom:2px}
.schedule p{font-size:19px;line-height:30px;white-space:nowrap}
.schedule em{font-style:normal;color:var(--yellow)}
.side-note{position:absolute;font-size:15px;font-weight:800;color:var(--yellow);line-height:1.3;text-align:center;width:110px}
.side-note.left{left:20px;top:640px}
.side-note.right{right:20px;top:640px}
.photo-bottom{position:absolute;background:linear-gradient(135deg,#d7c0b0,#8f7560);border:6px solid var(--white)}
.photo-bottom.left{left:30px;top:812px;width:270px;height:188px}
.photo-bottom.center{left:315px;top:806px;width:300px;height:196px}
.circle-note{position:absolute;right:30px;top:822px;width:200px;height:160px;border-radius:50%;background:var(--white);display:flex;align-items:center;justify-content:center;text-align:center;font-size:15px;font-weight:800;line-height:1.4;padding:20px}
.footer{position:absolute;left:0;top:1015px;width:867px;height:185px;background:var(--green)}
.visit{position:absolute;left:30px;top:1018px;font-size:14px;font-weight:800;color:var(--white)}
.contact-box{position:absolute;left:30px;top:1045px;width:400px;height:135px;background:var(--white);border-radius:10px;padding:12px 16px}
.contact-box .lead{font-size:28px;font-weight:900;color:var(--green-dark)}
.items{display:flex;align-items:center;gap:10px;margin-top:8px}
.items .tag{background:var(--green);color:var(--white);font-size:14px;font-weight:800;padding:6px 8px;border-radius:6px;line-height:1.2;text-align:center}
.items p{font-size:22px;font-weight:800;line-height:1.3}
.contact{position:absolute;left:460px;top:1045px;width:380px;height:135px;background:var(--white);border-radius:10px;padding:12px 18px;font-weight:800}
.contact .label{font-size:18px;color:var(--green-dark)}
.contact .org{font-size:24px}
.contact .role{font-size:16px}
.contact .tel{font-size:24px;color:var(--red);display:flex;align-items:center;gap:6px}
</style>
</head>
<body>
<div class="poster">
  <div class="header">
    <div class="kid left" role="img" aria-label="レシーブする子どものイラスト"></div>
    <div class="kid right" role="img" aria-label="スパイクする子どものイラスト"></div>
    <h1 class="title"><span>そうだ、</span><span>バレーボール、</span><span>しよう</span></h1>
    <p class="bubble-top left">レシーブ!スパイク!<br>きまると気持ちいい!</p>
    <p class="bubble-top right">チョウのようにまい!<br>ハチのようにさす!</p>
  </div>

  <div class="collage">
    <div class="photo tall" role="img" aria-label="練習中の選手たちの写真"></div>
    <div class="photo" role="img" aria-label="体育館でのチーム写真"></div>
    <div class="photo" role="img" aria-label="試合中の写真"></div>
    <div class="photo" role="img" aria-label="スパイク練習の写真"></div>
    <div class="photo" role="img" aria-label="応援する仲間の写真"></div>
  </div>

  <h2 class="club-name">大空バレースポーツ少年団</h2>
  <div class="recruit">男女新メンバー募集!!</div>

  <p class="side-note left">初めてでも<br>大歓迎!</p>
  <p class="side-note right">見学だけ<br>でもOK!</p>

  <section class="schedule">
    <h3>〜練習日(毎週)〜</h3>
    <p><em>★土・日曜日</em> / 9:00〜　大空小学校体育館・大空西小学校体育館</p>
    <p><em>★水曜日</em> / 17:30〜　大空小学校体育館</p>
  </section>

  <div class="photo-bottom left" role="img" aria-label="桜の前での集合写真"></div>
  <div class="photo-bottom center" role="img" aria-label="体育館での集合写真"></div>
  <div class="circle-note">いろいろな小学校から<br>通っている子も<br>いるよ!</div>

  <div class="footer"></div>
  <p class="visit">見学・体験はいつでも受け付けています!</p>
  <div class="contact-box">
    <p class="lead">連絡は担当:青木まで</p>
    <div class="items">
      <span class="tag">持ち<br>物</span>
      <p>上ぐつ・水とう<br>動きやすい服そう</p>
    </div>
  </div>
  <div class="contact">
    <p class="label">連絡先</p>
    <p class="org">大空バレースポーツ少年団</p>
    <p class="role">育成会 会長</p>
    <p class="tel">
      <svg width="22" height="22" viewBox="0 0 24 24" aria-hidden="true"><path fill="currentColor" d="M6.6 10.8a15 15 0 0 0 6.6 6.6l2.2-2.2a1 1 0 0 1 1-.25 11.4 11.4 0 0 0 3.6.57 1 1 0 0 1 1 1V20a1 1 0 0 1-1 1A17 17 0 0 1 3 4a1 1 0 0 1 1-1h3.5a1 1 0 0 1 1 1c0 1.250.2 2.450.57 3.57a1 1 0 0 1-.25 1z"/></svg>
      青木:090-0000-1234
    </p>
  </div>
</div>
</body>
</html>
```